Birchway Cleaning Commercial Flyer

Would like a flyer that will be used for making sales calls for commercial clients. These flyers will be handed out to Business Owners and facility managers. The flyer must peak interest, introduce the company, and give some information about our services. Birchway Cleaning Services (BWS) is a modern company that is eco-friendly. I have added what the uniform shirt looks like we have one in orange and one in blue. It would be nice to see the pictures you choose have the uniform on.

Target Market(s)

Office Mangers and Facility managers

Industry/Entity Type

Office Cleaning

Font styles to use
Serif

Colors
f78f20
0355a3
abd037

Requirements
Must have
• Modern clean look and feel. The flyer must straight forward and not busy.
• Have sections where bullet points or other written information can be placed
• Must be able to add and move information myself after the design has been decided on.
• Have a section that says:
• To learn more call 301-555-0148 or email info@birchway-tidyco.example
Nice to have
• Some pictures, clean and modern. Peak interest. The uniform to be photoshopped onto the models of the pictures
Should not have
• too busy

```html
<!DOCTYPE html>
<html lang="en">
<head>
<meta charset="utf-8">
<title>Birchway Cleaning Commercial Flyer</title>
<link rel="stylesheet" href="https://fonts.googleapis.com/css2?family=Archivo+Black&family=Montserrat:wght@400;600;700&display=swap">
<style>
  :root {
    --orange: #f78f20;
    --blue: #0355a3;
    --green: #abd037;
    --white: #ffffff;
    --ink: #1d1d1d;
    --stage: #5e5c5b;
    --photo-light: #eef4ee;
    --photo-mid: #c9dfd3;
  }
  * { margin: 0; padding: 0; box-sizing: border-box; }
  html, body { width: 1200px; height: 1044px; overflow: hidden; }
  body {
    background: var(--stage);
    font-family: "Montserrat", sans-serif;
    position: relative;
  }
  .flyer {
    position: absolute;
    left: 290px; top: 92px;
    width: 620px; height: 860px;
    background: var(--white);
    overflow: hidden;
    box-shadow: 0 18px 40px rgba(0,0,0,0.35);
  }
  .flyer-header {
    position: absolute; left: 0; top: 0; width: 100%; height: 112px;
    display: flex; align-items: center; gap: 16px; padding-left: 36px;
    background: var(--white);
    z-index: 3;
  }
  .brand-dot {
    width: 64px; height: 64px; border-radius: 50%;
    background: var(--blue);
  }
  .brand-name {
    font-family: "Montserrat", sans-serif;
    font-weight: 600;
    font-size: 30px;
    color: var(--blue);
  }
  .hero-photo {
    position: absolute; left: 0; top: 112px; width: 100%; height: 420px;
    background: linear-gradient(120deg, var(--white) 0%, var(--photo-light) 40%, var(--photo-mid) 100%);
  }
  .hero-copy {
    position: absolute; left: 36px; top: 132px; width: 480px; z-index: 2;
  }
  .audience {
    font-weight: 700; font-size: 17px; color: var(--ink);
    white-space: nowrap;
    margin-bottom: 14px;
  }
  .headline {
    font-family: "Archivo Black", sans-serif;
    font-size: 38px; line-height: 1.08;
    color: var(--blue);
    max-width: 420px;
  }
  .band-shapes {
    position: absolute; left: 0; top: 440px; width: 620px; height: 420px; z-index: 1;
  }
  .services {
    position: absolute; left: 40px; top: 592px; z-index: 2; color: var(--white);
  }
  .services-title {
    font-weight: 700; font-size: 24px; line-height: 1.25; letter-spacing: 0.5px; margin-bottom: 8px;
  }
  .services-list { list-style: none; }
  .services-list li {
    display: flex; align-items: center; gap: 10px;
    font-size: 16px; line-height: 1.7;
  }
  .services-list svg { flex: none; }
  .inset-photo {
    position: absolute; left: 420px; top: 410px;
    width: 168px; height: 168px; border-radius: 50%;
    border: 8px solid var(--white);
    background: linear-gradient(160deg, #3b4f78 0%, #8e9bb0 50%, #c9b89a 100%);
    z-index: 2;
  }
  .contact {
    position: absolute; right: 34px; bottom: 12px; z-index: 2;
    color: var(--white); text-align: right;
    font-size: 18px; line-height: 1.4;
  }
  .contact .phone { font-weight: 700; font-size: 25px; }
</style>
</head>
<body>
  <article class="flyer">
    <header class="flyer-header">
      <span class="brand-dot"></span>
      <span class="brand-name">Birchway Cleaning Services</span>
    </header>

    <div class="hero-photo" role="img" aria-label="Photo of a cleaner in a teal uniform mopping a bright office floor"></div>

    <div class="hero-copy">
      <p class="audience">Attention Business Owners and facility managers</p>
      <h1 class="headline">Birchway Cleaning Services offers eco-friendly cleaning at unbeatable rates.</h1>
    </div>

    <svg class="band-shapes" viewBox="0 0 620 420" aria-hidden="true">
      <polygon points="0,118 620,0 620,18 0,136" fill="var(--green)"/>
      <polygon points="0,136 620,18 620,330 0,330" fill="var(--blue)"/>
      <rect x="0" y="330" width="620" height="6" fill="var(--white)"/>
      <rect x="0" y="336" width="620" height="84" fill="var(--orange)"/>
    </svg>

    <div class="inset-photo" role="img" aria-label="Close-up photo of a flat mop cleaning an office floor"></div>

    <section class="services">
      <h2 class="services-title">OUR SERVICES:</h2>
      <ul class="services-list">
        <li><svg width="14" height="12" viewBox="0 0 14 12"><path d="M1 6l4 4 8-9" stroke="var(--green)" stroke-width="2.5" fill="none"/></svg>Hospital Grade disinfectants</li>
        <li><svg width="14" height="12" viewBox="0 0 14 12"><path d="M1 6l4 4 8-9" stroke="var(--green)" stroke-width="2.5" fill="none"/></svg>Eco-Friendly- microfiber cloths</li>
        <li><svg width="14" height="12" viewBox="0 0 14 12"><path d="M1 6l4 4 8-9" stroke="var(--green)" stroke-width="2.5" fill="none"/></svg>HEPA Backpack Vacuums</li>
        <li><svg width="14" height="12" viewBox="0 0 14 12"><path d="M1 6l4 4 8-9" stroke="var(--green)" stroke-width="2.5" fill="none"/></svg>Healthy Office/Work Environment is Happy Office</li>
      </ul>
    </section>

    <footer class="contact">
      <p>To learn more call <span class="phone">301-555-0148</span></p>
      <p>or email info@birchway-tidyco.example</p>
    </footer>
  </article>
</body>
</html>
```